Business card New design- upscale

Looking for modern design business cards. Minimalist, mix of gloss and matte finishes. Texas based Contractor company doing Mechanical hvac and plumbing, focused on commercial and industrial manufacturing facilities. We don't hand too many out so high end materials or functionality...will be considered. Please see attached files for info needed on cards. *New plumbing license needs to be edited to say K82917. Www.valtrimgroup.com
P.s. Website will also be redesigned soon.

Target Market(s)

Facility managers for commercial buildings, mechanical engineers for industrial manufacturing facilities including pharmaceutical, semiconductor, food & beverage, etc

Contact Information for Business Card

See attached images

Requirements
Must have
• All Logo colors: purple, black and Gray. 1, 2 or 4 rounded corners. All content on existing business cards (see attached images).
Nice to have
• Matte and gloss print. Embossing, raised print, functionality.
Should not have
• Stock images, generic construction.

```html
<!DOCTYPE html>
<html lang="en">
<head>
<meta charset="utf-8">
<title>Valtrim Group – Business Card</title>
<link href="https://fonts.googleapis.com/css2?family=Noto+Sans:wght@400;700&display=swap" rel="stylesheet">
<style>
  :root {
    --backdrop: #8f9196;
    --purple: #44286e;
    --purple-deep: #33205a;
    --paper: #e8e8ea;
    --ink-gray: #5f5f63;
    --white: #ffffff;
  }
  * { margin: 0; padding: 0; box-sizing: border-box; }
  html, body { width: 1200px; height: 900px; overflow: hidden; }
  body {
    position: relative;
    background: var(--backdrop);
    font-family: "Noto Sans", Verdana, sans-serif;
  }
  .card {
    position: absolute;
    left: 363px;
    width: 474px;
    height: 270px;
    border-radius: 18px;
    overflow: hidden;
  }
  .card-back { top: 145px; background: var(--purple); color: var(--white); }
  .card-front { top: 484px; background: var(--paper); }

  .brand-name {
    position: absolute;
    font-weight: 400;
    text-transform: uppercase;
    letter-spacing: 2px;
    white-space: nowrap;
  }
  .card-back .brand-name {
    left: 0; right: 0; top: 34px;
    text-align: center;
    font-size: 34px;
    color: var(--purple-deep);
  }
  .card-front .brand-name {
    left: 25px; top: 34px;
    font-size: 30px;
    color: var(--purple-deep);
  }

  .regulation {
    position: absolute;
    top: 125px;
    font-size: 11.5px;
    line-height: 15px;
    white-space: nowrap;
  }
  .regulation-plumbing { right: 250px; text-align: right; }
  .regulation-licensing { left: 250px; }
  .regulation-divider {
    position: absolute;
    left: 236px; top: 128px;
    width: 1.5px; height: 115px;
    background: var(--white);
  }

  .person-name {
    position: absolute;
    right: 26px; top: 128px;
    font-size: 14px; font-weight: 700;
    color: var(--purple-deep);
    letter-spacing: 0.3px;
  }
  .person-title {
    position: absolute;
    right: 26px; top: 145px;
    font-size: 12px;
    color: var(--ink-gray);
  }
  .name-rule {
    position: absolute;
    left: 25px; top: 154px;
    width: 212px; height: 1.5px;
    background: var(--purple-deep);
  }
  .contact-list {
    position: absolute;
    left: 25px; top: 166px;
    list-style: none;
    font-size: 12px;
    line-height: 15.3px;
    color: var(--ink-gray);
  }
  .contact-list li { display: flex; align-items: center; gap: 7px; }
  .contact-list svg { width: 9px; height: 9px; fill: var(--purple-deep); flex: none; }
  .site-core { color: var(--purple-deep); }
  .address {
    position: absolute;
    right: 26px; top: 197px;
    text-align: right;
    font-size: 12px;
    line-height: 15.3px;
    color: var(--ink-gray);
  }
  .service-band {
    position: absolute;
    left: 0; right: 0; bottom: 0;
    height: 31px;
    background: var(--purple);
    color: var(--white);
    font-size: 12px;
    display: flex; align-items: center; justify-content: center;
    gap: 10px;
  }
  .band-divider { width: 1.5px; height: 15px; background: var(--white); }
</style>
</head>
<body>
  <section class="card card-back">
    <div class="brand-name">Valtrim Group</div>
    <div class="regulation regulation-plumbing">
      RMP-48190<br>
      Regulated by the<br>
      Lone Star Board of<br>
      Pipe Examiners,<br>
      P.O. Box 3300,<br>
      Austin, TX. 78701;<br>
      1-800-555-0142,<br>
      512-555-0187/ TACLA60312B
    </div>
    <div class="regulation-divider"></div>
    <div class="regulation regulation-licensing">
      Regulated by the<br>
      Lone Star Office of<br>
      Trade Licensing,<br>
      P.O. Box 14020,<br>
      Austin, TX. 78703;<br>
      1-800-555-0199,<br>
      512-555-0123<br>
      www.tradelicense.example.us
    </div>
  </section>

  <section class="card card-front">
    <div class="brand-name">Valtrim Group</div>
    <div class="person-name">DALE MORROW</div>
    <div class="person-title">Lead Estimator/Sr. Project Manager</div>
    <div class="name-rule"></div>
    <ul class="contact-list">
      <li><svg viewBox="0 0 10 10" aria-hidden="true"><path d="M2.5 0h5a1 1 0 0 1 1 1v8a1 1 0 0 1-1 1h-5a1 1 0 0 1-1-1V1a1 1 0 0 1 1-1zm.5 1.2v6.6h4V1.2z"/></svg>(555) 214-7730</li>
      <li><svg viewBox="0 0 10 10" aria-hidden="true"><path d="M2 0.5l2 2.2-1 1.3c.6 1.3 1.6 2.3 2.9 2.9l1.3-1 2.2 2-1.2 1.6C4.7 9.3.7 5.3.4 1.7z"/></svg>(555) 309-4416</li>
      <li><svg viewBox="0 0 10 10" aria-hidden="true"><path d="M0 2h10v6H0zM0.8 2.6L5 5.6l4.2-3v.9L5 6.5.8 3.5z"/></svg>dmorrow@valtrimgroup.com</li>
      <li><svg viewBox="0 0 10 10" aria-hidden="true"><circle cx="5" cy="5" r="4.8"/></svg>www.<span class="site-core">valtrimgroup</span>.com</li>
    </ul>
    <div class="address">2180 Cedar Ridge Rd.<br>Arlington, TX 76018</div>
    <div class="service-band">
      <span>Commercial &amp; Industrial Contactors</span>
      <span class="band-divider"></span>
      <span>Mechanical &amp; Plumbing Services</span>
    </div>
  </section>
</body>
</html>
```